Website redesign

Looking to redesign our existing website. (hire4ward.com.au)
New design needs to be bright, fun and have an easy flowing.
The website needs to be design with call to action.

Some examples of other websites:
brightdesk.com
lendnest.com.au

We are happy with the content of our existing website.

Target Market(s)

other businesses

Industry/Entity Type

Business Service

Number of Pages Required

5+ page

Requirements
Must have
• Theme redesign
Cool animation similar to brightdesk.com

```html
<!DOCTYPE html>
<html lang="en">
<head>
<meta charset="utf-8">
<title>Hire 4ward – News &amp; Articles</title>
<link href="https://fonts.googleapis.com/css2?family=Poppins:wght@400;500;600;700&display=swap" rel="stylesheet">
<style>
:root{
  --navy:#0f1f33;
  --navy-2:#13253b;
  --blue:#0ba5e0;
  --ink:#14202e;
  --grey:#7a7f87;
  --line:#e6e8eb;
  --white:#ffffff;
}
*{box-sizing:border-box;margin:0;padding:0}
html,body{width:720px;height:1200px;overflow:hidden;background:var(--white);font-family:"Poppins",sans-serif;color:var(--ink)}
.page{position:relative;width:720px;height:1200px;overflow:hidden}
.abs{position:absolute}

/* top bar */
.topbar{left:0;top:0;width:720px;height:24px;background:var(--navy);color:#dfe6ee;font-size:6.6px}
.topbar .info{position:absolute;top:0;height:24px;display:flex;align-items:center;gap:4px}
.topbar svg{width:8px;height:8px;fill:var(--blue)}
.topbar .social{position:absolute;left:522px;top:9px;display:flex;gap:4px}
.topbar .social span{width:5px;height:5px;border-radius:50%;background:#dfe6ee}
.btn-top{position:absolute;left:569px;top:3px;width:54px;height:18px;background:var(--blue);color:#fff;font-size:6.6px;display:flex;align-items:center;justify-content:center}

/* header */
.header{left:0;top:24px;width:720px;height:39px;background:#fff}
.brand{position:absolute;left:97px;top:7px;font-weight:600;font-size:10px;line-height:1;color:var(--ink);display:flex;align-items:center;gap:4px}
.brand i{width:9px;height:9px;border-radius:50%;background:var(--blue);display:block}
.nav{position:absolute;top:15px;font-size:6.6px;font-weight:500;color:var(--ink)}
.nav .caret{font-size:5px;margin-left:2px}
.menu-tab{position:absolute;left:582px;top:0;width:66px;height:39px}

/* hero */
.hero{left:0;top:63px;width:720px;height:101px;background:linear-gradient(100deg,#5c5d61 0%,#3d3f44 45%,#26272b 100%)}
.crumb{position:absolute;left:97px;top:33px;display:flex;align-items:center;gap:8px;color:#fff;font-size:8px;font-weight:500}
.crumb b{width:22px;height:2px;background:var(--blue);display:block}
.hero h1{position:absolute;left:96px;top:48px;color:#fff;font-size:18.5px;font-weight:700}

/* section head */
.badge{left:344px;top:211px;width:31px;height:14px;border-radius:7px;background:var(--blue);color:#fff;font-size:6px;display:flex;align-items:center;justify-content:center}
.badge:after{content:"";position:absolute;left:13px;bottom:-3px;border:3px solid transparent;border-top-color:var(--blue);border-bottom:0}
.section-title{left:0;top:230px;width:720px;text-align:center;font-size:14.5px;font-weight:600}
.section-lead{left:200px;top:260px;width:320px;text-align:center;font-size:6.9px;line-height:10.8px;color:var(--grey)}

/* cards */
.card{position:absolute;width:254px;height:166px;display:flex}
.card .photo{position:relative;width:127px;height:166px}
.card .photo .mark{position:absolute;left:117px;top:0;width:1px;height:38px;background:var(--blue)}
.card .read{position:absolute;left:0;top:20px;width:67px;height:26px;background:#fff;color:var(--blue);font-size:6.8px;display:flex;align-items:center;justify-content:center}
.card .body{width:127px;height:166px;background:#fff;box-shadow:0 2px 8px rgba(0,0,0,.08);padding:10px 9px 0}
.card h3{font-size:9.2px;line-height:13.6px;font-weight:500;color:var(--ink)}
.card p{margin-top:5px;font-size:6.7px;line-height:10.8px;color:var(--grey);height:86px;overflow:hidden}
.card .meta{margin-top:2px;border-top:1px solid var(--line);padding-top:4px;font-size:6.5px;font-weight:500;color:#4a525c;display:flex;align-items:center;gap:3px;width:98px}
.card .meta svg{width:6px;height:6px;fill:var(--blue)}
.card .meta .sep{width:1px;height:7px;background:var(--line);margin:0 2px}
.ph-sofa{background:linear-gradient(160deg,#6c6f74 0%,#4b4d51 45%,#6d5a44 75%,#e5e6e8 100%)}
.ph-laptop{background:linear-gradient(150deg,#e9e7e3 0%,#2b2f36 45%,#1a1d22 60%,#c9b49a 100%)}
.ph-team{background:linear-gradient(160deg,#eef1f4 0%,#c9cfd6 40%,#9a8578 70%,#2b2a2c 100%)}
.ph-portrait{background:linear-gradient(160deg,#8f7f68 0%,#3b3632 45%,#1c1c1e 70%,#c6a63a 100%)}

/* pagination */
.pager{left:282px;top:851px;display:flex;gap:3px}
.pager span{width:29px;height:27px;background:var(--navy);color:#fff;font-size:8.5px;display:flex;align-items:center;justify-content:center}
.pager span.active{background:var(--blue)}
.pager svg{width:8px;height:8px;stroke:#fff;stroke-width:2;fill:none}

/* footer */
.footer{left:0;top:929px;width:720px;height:271px;background:linear-gradient(180deg,var(--navy-2),var(--navy));color:#c8d1db}
.footer .brand{left:97px;top:36px;color:#fff}
.f-text{position:absolute;font-size:6.7px;line-height:12.6px;color:#c8d1db}
.f-head{position:absolute;top:38px;font-size:8.3px;font-weight:600;color:#fff}
.f-head:after{content:"";position:absolute;left:0;top:17px;width:14px;height:1px;background:var(--blue)}
.f-social{position:absolute;left:97px;top:128px;display:flex;gap:9px}
.f-social span{width:6px;height:6px;border-radius:50%;background:#fff}
.f-btn{position:absolute;left:97px;top:147px;width:54px;height:22px;background:var(--blue);color:#fff;font-size:6.6px;display:flex;align-items:center;justify-content:center}
.links{position:absolute;left:233px;top:63px;list-style:none;font-size:6.7px;line-height:12.6px}
.links li{display:flex;align-items:center;gap:5px}
.links li:before{content:"";width:6px;height:6px;border-radius:50%;border:2px solid #c8d1db;box-sizing:border-box}
.post{position:absolute;left:324px;display:flex;gap:6px}
.post .thumb{width:31px;height:31px;border-radius:50%;border:2px solid #fff;background:linear-gradient(160deg,#6c6f74,#4b4d51 55%,#e5e6e8)}
.post .date{font-size:6px;color:#c8d1db;display:flex;align-items:center;gap:3px}
.post .date i{width:5px;height:5px;border-radius:50%;background:var(--blue);display:block}
.post .t{font-size:6.7px;line-height:11px;margin-top:3px;color:#dfe6ee}
.c-row{position:absolute;left:505px;display:flex;align-items:center;gap:5px;font-size:6.7px;color:#dfe6ee}
.c-row svg{width:12px;height:12px}
.subscribe{left:235px;top:176px;width:250px;height:36px;background:#fff;padding:7px 5px}
.subscribe .field{position:absolute;left:6px;top:7px;width:177px;height:22px;border:1px solid var(--line);font-size:6.5px;color:#9aa1a9;display:flex;align-items:center;padding-left:10px}
.subscribe .go{position:absolute;left:183px;top:7px;width:62px;height:22px;background:var(--blue);color:#fff;font-size:6.3px;font-weight:500;display:flex;align-items:center;justify-content:center}
.f-rule{left:0;top:242px;width:720px;height:1px;background:#26384e}
.copy{left:0;top:251px;width:720px;text-align:center;font-size:6.3px;font-weight:500;color:#fff}
</style>
</head>
<body>
<div class="page">

  <div class="abs topbar">
    <div class="info" style="left:97px"><svg viewBox="0 0 24 24"><path d="M6.6 10.8a15 15 0 0 0 6.6 6.6l2.2-2.2c.3-.3.7-.4 1-.2 1.1.4 2.3.6 3.6.6.6 0 1 .4 1 1V20c0 .6-.4 1-1 1A17 17 0 0 1 3 4c0-.6.4-1 1-1h3.5c.6 0 1 .4 1 1 0 1.3.2 2.5.6 3.6.1.3 0 .7-.2 1z"/></svg>Phone: +1 123-456-7890</div>
    <div class="info" style="left:210px"><svg viewBox="0 0 24 24"><path d="M2 6l10 7 10-7v12H2z M2 5h20l-10 7z"/></svg>Email: info@example.com</div>
    <div class="info" style="left:327px"><svg viewBox="0 0 24 24"><path d="M12 2a10 10 0 1 0 0 20 10 10 0 0 0 0-20zm1 10.4V6h-2v7.2l5 3 1-1.7z"/></svg>Opening: 08:00-08:00</div>
    <div class="social"><span></span><span></span><span></span><span></span></div>
    <div class="btn-top">Contact Us</div>
  </div>

  <div class="abs header">
    <div class="brand"><i></i>HIRE 4WARD</div>
    <div class="nav" style="left:337px">Home</div>
    <div class="nav" style="left:369px">About Us</div>
    <div class="nav" style="left:408px">Tips And Tricks<span class="caret">&#9662;</span></div>
    <div class="nav" style="left:475px">Our Services<span class="caret">&#9662;</span></div>
    <div class="nav" style="left:534px">Contact Us</div>
    <svg class="menu-tab" viewBox="0 0 66 39">
      <polygon points="18,0 66,0 48,39 0,39" fill="#0ba5e0"/>
      <circle cx="33" cy="19.5" r="6" fill="none" stroke="#fff" stroke-width="1"/>
      <path d="M30.5 17.5h5M30.5 19.5h5M30.5 21.5h5" stroke="#fff" stroke-width="0.9"/>
    </svg>
  </div>

  <div class="abs hero" role="img" aria-label="Photo of hands typing on a laptop keyboard">
    <div class="crumb"><b></b>Home &#8250; Blog</div>
    <h1>News &amp; Articles</h1>
  </div>

  <div class="abs badge">Latest</div>
  <div class="abs section-title">News &amp; Articles</div>
  <div class="abs section-lead">Aliquam Sodales Justo Sit Amet Urna Auctor Scelerisquinterdum Leo Anet Tempus Enim Esent Egetis Hendrerit Vel Nibh Vitae Ornar Sem Velit Aliquam</div>

  <article class="card" style="left:97px;top:291px">
    <div class="photo ph-sofa" role="img" aria-label="Photo of a grey armchair on a woven rug"><span class="mark"></span><span class="read">Read More</span></div>
    <div class="body"><h3>Lorem Ipsum Dolor Sit Amet, Conse Ctetur Adipiscing Eli</h3><p>Sed tempus pulvinar augue ut euismod. Donec a nisi volutpat, dignissim mauris eget. Quisque vitae nunc sit amet eros pellentesque tempus at sit amet sem. Maecenas feugiat mauris Sed tempus pulvinar augue ut euismod.</p><div class="meta"><svg viewBox="0 0 10 10"><path d="M1 2h8v7H1zM2 0h1v2H2zM7 0h1v2H7z"/></svg>August<span class="sep"></span><svg viewBox="0 0 10 10"><path d="M0 1h7v5H3L1 8V6H0zM8 3h2v5H9v2L7 8H4V7h4z"/></svg>0</div></div>
  </article>
  <article class="card" style="left:369px;top:291px">
    <div class="photo ph-laptop" role="img" aria-label="Photo of a laptop showing code beside a small plant"><span class="mark"></span></div>
    <div class="body"><h3>Lorem Ipsum Dolor Sit Amet, Conse Ctetur Adipiscing Eli</h3><p>Sed tempus pulvinar augue ut euismod. Donec a nisi volutpat, dignissim mauris eget. Quisque vitae nunc sit amet eros pellentesque tempus at sit amet sem. Maecenas feugiat mauris Sed tempus pulvinar augue ut euismod.</p><div class="meta"><svg viewBox="0 0 10 10"><path d="M1 2h8v7H1zM2 0h1v2H2zM7 0h1v2H7z"/></svg>August<span class="sep"></span><svg viewBox="0 0 10 10"><path d="M0 1h7v5H3L1 8V6H0zM8 3h2v5H9v2L7 8H4V7h4z"/></svg>0</div></div>
  </article>
  <article class="card" style="left:97px;top:476px">
    <div class="photo ph-team" role="img" aria-label="Photo of a team meeting being filmed"><span class="mark"></span></div>
    <div class="body"><h3>Lorem Ipsum Dolor Sit Amet, Conse Ctetur Adipiscing Eli</h3><p>Sed tempus pulvinar augue ut euismod. Donec a nisi volutpat, dignissim mauris eget. Quisque vitae nunc sit amet eros pellentesque tempus at sit amet sem. Maecenas feugiat mauris Sed tempus pulvinar augue ut euismod.</p><div class="meta"><svg viewBox="0 0 10 10"><path d="M1 2h8v7H1zM2 0h1v2H2zM7 0h1v2H7z"/></svg>August<span class="sep"></span><svg viewBox="0 0 10 10"><path d="M0 1h7v5H3L1 8V6H0zM8 3h2v5H9v2L7 8H4V7h4z"/></svg>0</div></div>
  </article>
  <article class="card" style="left:369px;top:476px">
    <div class="photo ph-portrait" role="img" aria-label="Portrait photo of a smiling team member in an office"><span class="mark"></span></div>
    <div class="body"><h3>Lorem Ipsum Dolor Sit Amet, Conse Ctetur Adipiscing Eli</h3><p>Sed tempus pulvinar augue ut euismod. Donec a nisi volutpat, dignissim mauris eget. Quisque vitae nunc sit amet eros pellentesque tempus at sit amet sem. Maecenas feugiat mauris Sed tempus pulvinar augue ut euismod.</p><div class="meta"><svg viewBox="0 0 10 10"><path d="M1 2h8v7H1zM2 0h1v2H2zM7 0h1v2H7z"/></svg>August<span class="sep"></span><svg viewBox="0 0 10 10"><path d="M0 1h7v5H3L1 8V6H0zM8 3h2v5H9v2L7 8H4V7h4z"/></svg>0</div></div>
  </article>
  <article class="card" style="left:97px;top:661px">
    <div class="photo ph-sofa" role="img" aria-label="Photo of a grey armchair on a woven rug"><span class="mark"></span></div>
    <div class="body"><h3>Lorem Ipsum Dolor Sit Amet, Conse Ctetur Adipiscing Eli</h3><p>Sed tempus pulvinar augue ut euismod. Donec a nisi volutpat, dignissim mauris eget. Quisque vitae nunc sit amet eros pellentesque tempus at sit amet sem. Maecenas feugiat mauris Sed tempus pulvinar augue ut euismod.</p><div class="meta"><svg viewBox="0 0 10 10"><path d="M1 2h8v7H1zM2 0h1v2H2zM7 0h1v2H7z"/></svg>August<span class="sep"></span><svg viewBox="0 0 10 10"><path d="M0 1h7v5H3L1 8V6H0zM8 3h2v5H9v2L7 8H4V7h4z"/></svg>0</div></div>
  </article>
  <article class="card" style="left:369px;top:661px">
    <div class="photo ph-laptop" role="img" aria-label="Photo of a laptop showing code beside a small plant"><span class="mark"></span></div>
    <div class="body"><h3>Lorem Ipsum Dolor Sit Amet, Conse Ctetur Adipiscing Eli</h3><p>Sed tempus pulvinar augue ut euismod. Donec a nisi volutpat, dignissim mauris eget. Quisque vitae nunc sit amet eros pellentesque tempus at sit amet sem. Maecenas feugiat mauris Sed tempus pulvinar augue ut euismod.</p><div class="meta"><svg viewBox="0 0 10 10"><path d="M1 2h8v7H1zM2 0h1v2H2zM7 0h1v2H7z"/></svg>August<span class="sep"></span><svg viewBox="0 0 10 10"><path d="M0 1h7v5H3L1 8V6H0zM8 3h2v5H9v2L7 8H4V7h4z"/></svg>0</div></div>
  </article>

  <div class="abs pager">
    <span><svg viewBox="0 0 10 10"><path d="M6.5 1.5 3 5l3.5 3.5"/></svg></span>
    <span>1</span><span class="active">2</span><span>3</span>
    <span><svg viewBox="0 0 10 10"><path d="M3.5 1.5 7 5 3.5 8.5"/></svg></span>
  </div>

  <footer class="abs footer">
    <div class="brand abs"><i></i>HIRE 4WARD</div>
    <div class="f-text" style="left:97px;top:64px;width:112px">Beatae vitae dicta su explicabo nemo enim ipsam voluptatem quia voluptas sitBeatae vitae sit-Beatae vitae dicta suntania.</div>
    <div class="f-social"><span></span><span></span><span></span><span></span><span></span></div>
    <div class="f-btn">About Us</div>

    <div class="f-head" style="left:233px">Useful Links</div>
    <ul class="links"><li>About</li><li>Our Services</li><li>Our Team</li><li>Blog</li><li>Contact</li></ul>

    <div class="f-head" style="left:324px">Blog Page</div>
    <div class="post" style="top:65px"><div class="thumb" role="img" aria-label="Blog thumbnail of an armchair"></div><div><div class="date"><i></i>August 16, 2020</div><div class="t">Beatae vitae dicta sunt explicabo<br>nemo enim ipsam voluptatem</div></div></div>
    <div class="post" style="top:109px"><div class="thumb" role="img" aria-label="Blog thumbnail of an armchair"></div><div><div class="date"><i></i>August 16, 2020</div><div class="t">Beatae vitae dicta sunt explicabo<br>nemo enim ipsam voluptatem</div></div></div>

    <div class="f-head" style="left:505px">Contact</div>
    <div class="f-text" style="left:505px;top:63px">Beatae vitae dicta sunt explicabo<br>nemo enim ipsam voluptatem</div>
    <div class="c-row" style="top:94px"><svg viewBox="0 0 24 24"><circle cx="12" cy="12" r="11" fill="none" stroke="#dfe6ee"/><path d="M8.5 7.5l2 2-1 1.5a7 7 0 0 0 3.5 3.5l1.5-1 2 2-1.5 1.5A9 9 0 0 1 7 9z" fill="#dfe6ee"/></svg>(+1) 123-456-7890</div>
    <div class="c-row" style="top:113px"><svg viewBox="0 0 24 24"><circle cx="12" cy="12" r="11" fill="none" stroke="#dfe6ee"/><path d="M7 8.5h10v7H7z M7 8.5l5 4 5-4" fill="#dfe6ee" stroke="#13253b" stroke-width=".8"/></svg>Lorem ipsum dolor sit amet,</div>
    <div class="c-row" style="top:131px"><svg viewBox="0 0 24 24"><circle cx="12" cy="12" r="11" fill="none" stroke="#dfe6ee"/><path d="M12 6a4 4 0 0 0-4 4c0 3 4 8 4 8s4-5 4-8a4 4 0 0 0-4-4zm0 5.5a1.5 1.5 0 1 1 0-3 1.5 1.5 0 0 1 0 3z" fill="#dfe6ee"/></svg>Lorem ipsum dolor sit amet,</div>

    <div class="abs subscribe"><div class="field">Enter Your Email Address</div><div class="go">SUBSCRIBE</div></div>
    <div class="abs f-rule"></div>
    <div class="abs copy">© 2020 HIRE 4WARD | ALL RIGHTS RESERVED.</div>
  </footer>
</div>
</body>
</html>
```